Christmas Flyer for a Newspaper Insert

Lumo Eyewear - Logo Attached

Lumo Eyewear is looking for a flyer design that will be inserted in a local newspaper and distributed to over 160,000 consumers. Lumo is an eyewear company that does designer prescription glasses, and designer sunwear. We have brands such as Brackwell, Sunvex, Velko, Luvé, Martolli, Kona Ted, etc.... The size should be 8.5 x 5.5. The end design will need to be printed twice on an 8.5 x 11 piece of paper and then cut in two.

Our offer is buy one get one at 50% off.
Restrictions are: not valid with some insurance plans

The look of Lumo is techy,somewhat industrial, and we use alot of silver, black and red. Our look is similar to Brackwell at Brackwell.com.
Updates

We will make a decision today on all designs and will need the high res art very fast.

Industry/Entity Type

Eyewear

Requirements
Must have
• Look at ads on Brackwell's website at Brackwell.com to get the look and feel.
Nice to have
• 5 Locations - Fairbrook, Millgate Plaza, Harborline, Ashvale, Crestmoor
• Website www.lumorxopt.example

```html
<!DOCTYPE html>
<html lang="en">
<head>
<meta charset="utf-8">
<title>Lumo Eyewear – Buy One Get One 50% Flyer</title>
<link rel="stylesheet" href="https://fonts.googleapis.com/css2?family=Russo+One&family=Michroma&display=swap">
<style>
  :root {
    --bg-deep: #050505;
    --bg-mid: #262626;
    --red-bright: #ff2a22;
    --red-deep: #8e0a08;
    --silver-light: #ffffff;
    --silver-dark: #8a8a8a;
    --text-light: #e8e8e8;
    --text-muted: #bdbdbd;
    --accent-red: #e3201b;
  }
  * { margin: 0; padding: 0; box-sizing: border-box; }
  html, body {
    width: 1200px;
    height: 776px;
    overflow: hidden;
    background: var(--bg-deep);
  }
  .flyer {
    position: relative;
    width: 1200px;
    height: 776px;
    overflow: hidden;
    background:
      radial-gradient(ellipse 520px 300px at 600px 250px, rgba(80,80,80,0.55), transparent 70%),
      radial-gradient(ellipse 900px 500px at 600px 200px, var(--bg-mid), var(--bg-deep) 80%);
    font-family: "Michroma", sans-serif;
    color: var(--text-light);
  }
  .glare {
    position: absolute;
    left: 100px;
    top: 230px;
    width: 1000px;
    height: 140px;
    background: radial-gradient(ellipse 50% 30% at 50% 50%, rgba(255,40,30,0.55), transparent 75%);
  }
  .eyewear-photo {
    position: absolute;
    top: 150px;
    width: 270px;
    height: 150px;
    border-radius: 40% 40% 50% 50% / 35% 35% 60% 60%;
    background: linear-gradient(160deg, #6a6a6a 0%, #1a1a1a 45%, #0a0a0a 70%, #4a4a4a 100%);
  }
  .eyewear-photo--left { left: 110px; transform: rotate(-8deg); }
  .eyewear-photo--right { left: 840px; transform: rotate(8deg) scaleX(-1); }
  .headline {
    position: absolute;
    left: 0;
    top: 140px;
    width: 1200px;
    height: 320px;
  }
  .headline text { font-family: "Russo One", sans-serif; }
  .details {
    position: absolute;
    left: 0;
    top: 496px;
    width: 1200px;
    text-align: center;
    font-size: 14px;
    line-height: 32px;
    letter-spacing: 0.5px;
  }
  .details .locations span.divider { color: var(--text-muted); padding: 0 10px; }
  .details .website { font-size: 13px; }
  .details .website .highlight { color: var(--accent-red); }
  .brand {
    position: absolute;
    left: 0;
    top: 636px;
    width: 1200px;
    text-align: center;
  }
  .brand-name {
    font-family: "Michroma", sans-serif;
    font-size: 24px;
    line-height: 32px;
    color: var(--text-light);
  }
  .brand-tagline {
    margin-top: 16px;
    font-size: 12px;
    letter-spacing: 1px;
    color: var(--text-muted);
  }
</style>
</head>
<body>
<main class="flyer">
  <div class="glare"></div>
  <div class="eyewear-photo eyewear-photo--left" role="img" aria-label="Product photo of black wraparound sport sunglasses"></div>
  <div class="eyewear-photo eyewear-photo--right" role="img" aria-label="Product photo of black wraparound sport sunglasses"></div>

  <svg class="headline" viewBox="0 140 1200 320" aria-label="50% Special Offer – Buy One Get One">
    <defs>
      <linearGradient id="red-metal" x1="0" y1="0" x2="0" y2="1">
        <stop offset="0" stop-color="#ff2a22"/>
        <stop offset="0.55" stop-color="#d01510"/>
        <stop offset="1" stop-color="#8e0a08"/>
      </linearGradient>
      <linearGradient id="silver-metal" x1="0" y1="0" x2="0" y2="1">
        <stop offset="0" stop-color="#ffffff"/>
        <stop offset="0.5" stop-color="#d6d6d6"/>
        <stop offset="0.52" stop-color="#a5a5a5"/>
        <stop offset="1" stop-color="#8a8a8a"/>
      </linearGradient>
    </defs>
    <text x="600" y="258" text-anchor="middle" font-size="134" textLength="440" lengthAdjust="spacingAndGlyphs" fill="url(#red-metal)">50%</text>
    <text x="600" y="362" text-anchor="middle" font-size="86" textLength="880" lengthAdjust="spacingAndGlyphs" fill="url(#red-metal)">SPECIAL OFFER</text>
    <text x="600" y="440" text-anchor="middle" font-size="92" textLength="900" lengthAdjust="spacingAndGlyphs" fill="url(#silver-metal)">BUY ONE GET ONE</text>
  </svg>

  <section class="details">
    <p class="restrictions">Restrictions are: not valid with some insurance plans</p>
    <p class="locations">Fairbrook<span class="divider">|</span>Millgate Plaza<span class="divider">|</span>Harborline<span class="divider">|</span>Ashvale<span class="divider">|</span>Crestmoor Website</p>
    <p class="website">www.<span class="highlight">lumorxopt</span>.example</p>
  </section>

  <footer class="brand">
    <div class="brand-name">Lumo</div>
    <div class="brand-tagline">Clear sight for every day</div>
  </footer>
</main>
</body>
</html>
```